Modern/Bold/Unique Prenatal Vitamin label redesign

We are in need of a design update for our Prenatal Vitamin label. We want to modernize our label and give it a fresh feel.
It should bring a feeling of fun, joy, and sophistication, but also be bold/edgy/unique and portray Trust and Authority. Our buyers are mainly mothers in the age range of 25-34 who are pregnant or breastfeeding.
I will attach our current label design, as well as some inspiration to go off of.
We like the idea of having a clean, easy to read label label with bold/vibrant colors and fonts. We like the idea of having some retro vibes in it as well
Please see the attached artwork for design inspiration (New Design Idea). We like the idea of having a pregnant mother image like the attachment on the label, with the rest of the label being white. Please come up with a unique drawing/image for the design. We cannot use a copied image or stock image.
We look forward to working with you!

```html
<!DOCTYPE html>
<html lang="en">
<head>
<meta charset="utf-8">
<title>Nurture Plus – Prenatal Label</title>
<link rel="stylesheet" href="https://fonts.googleapis.com/css2?family=Montserrat:wght@600;700&family=Montserrat+Alternates:wght@700&display=swap">
<style>
  :root {
    --green-top: #3bb64b;
    --green-mid: #0a9845;
    --green-bottom: #066f38;
    --white: #ffffff;
    --figure-light: #f1f5f2;
    --figure-mid: #cfe6d4;
    --page: #ffffff;
  }
  html, body {
    margin: 0;
    padding: 0;
    width: 1200px;
    height: 1000px;
    overflow: hidden;
    background: var(--page);
  }
  .canvas {
    position: relative;
    width: 1200px;
    height: 1000px;
  }
  .label {
    position: absolute;
    left: 210px;
    top: 82px;
    width: 813px;
    height: 813px;
    background: linear-gradient(180deg, var(--green-top) 0%, var(--green-mid) 55%, var(--green-bottom) 100%);
    color: var(--white);
    overflow: hidden;
  }
  .divider {
    position: absolute;
    left: 204px;
    top: 0;
    width: 7px;
    height: 100%;
    background: var(--white);
  }
  .claims {
    position: absolute;
    left: 0;
    top: 0;
    width: 204px;
    height: 100%;
    font-family: "Montserrat", sans-serif;
    text-align: center;
  }
  .claim {
    position: absolute;
    left: 0;
    width: 204px;
  }
  .claim svg { display: block; margin: 0 auto; }
  .claim-vegan { top: 296px; }
  .claim-vegan .claim-text {
    font-size: 27px;
    font-weight: 600;
    letter-spacing: 0.5px;
    margin-top: -8px;
    padding-left: 30px;
  }
  .claim-gmp { top: 418px; }
  .claim-gmp .claim-title {
    font-size: 24px;
    font-weight: 700;
    letter-spacing: 1px;
  }
  .claim-gmp .claim-sub {
    font-size: 16px;
    font-weight: 600;
    margin-top: -2px;
  }
  .claim-allergen { top: 506px; }
  .claim-allergen .claim-text {
    font-size: 15px;
    font-weight: 600;
    line-height: 21px;
    margin-top: 6px;
  }
  .claim-nongmo { top: 660px; }
  .claim-nongmo .claim-text {
    font-size: 23px;
    font-weight: 600;
    letter-spacing: 0.5px;
    margin-top: 10px;
  }
  .brand {
    position: absolute;
    left: 288px;
    top: 36px;
    font-family: "Montserrat Alternates", sans-serif;
    font-weight: 700;
    font-size: 42px;
    letter-spacing: -0.5px;
  }
  .hero-art {
    position: absolute;
    left: 296px;
    top: 130px;
    width: 320px;
    height: 290px;
  }
  .product-name {
    position: absolute;
    left: 288px;
    top: 440px;
    margin: 0;
    font-family: "Montserrat Alternates", sans-serif;
    font-weight: 700;
    font-size: 57px;
    letter-spacing: -0.5px;
  }
  .tagline {
    position: absolute;
    left: 288px;
    top: 522px;
    margin: 0;
    font-family: "Montserrat", sans-serif;
    font-weight: 700;
    font-size: 21px;
    line-height: 33px;
  }
  .count {
    position: absolute;
    left: 528px;
    top: 700px;
    display: flex;
    align-items: center;
    font-family: "Montserrat", sans-serif;
    font-weight: 700;
  }
  .count-number {
    font-family: "Montserrat Alternates", sans-serif;
    font-size: 64px;
    line-height: 1;
    margin-right: 14px;
  }
  .count-unit {
    font-size: 20px;
    line-height: 24px;
  }
</style>
</head>
<body>
<div class="canvas">
  <section class="label">
    <aside class="claims">
      <div class="claim claim-vegan">
        <svg width="80" height="40" viewBox="0 0 80 40" aria-hidden="true">
          <path d="M6 22 C 20 6, 40 10, 44 30 C 28 32, 14 30, 6 22 Z" fill="var(--white)"/>
          <path d="M44 28 C 48 10, 62 4, 76 4 C 74 20, 62 28, 44 28 Z" fill="var(--white)"/>
        </svg>
        <div class="claim-text">VEGAN</div>
      </div>
      <div class="claim claim-gmp">
        <div class="claim-title">★ GMP ★</div>
        <div class="claim-sub">Quality Assured</div>
      </div>
      <div class="claim claim-allergen">
        <svg width="34" height="34" viewBox="0 0 34 34" aria-hidden="true">
          <circle cx="17" cy="17" r="16" fill="var(--white)"/>
          <path d="M8 22 C 10 12, 16 10, 22 10 C 22 18, 16 23, 8 22 Z" fill="var(--green-mid)"/>
          <path d="M14 26 C 18 18, 24 16, 28 16 C 26 23, 20 26, 14 26 Z" fill="var(--green-mid)"/>
        </svg>
        <div class="claim-text">GLUTEN<br>AND MAJOR<br>ALLERGEN FREE</div>
      </div>
      <div class="claim claim-nongmo">
        <svg width="140" height="58" viewBox="0 0 140 58" aria-hidden="true">
          <path d="M4 20 C 30 6, 58 16, 66 54 C 36 54, 14 44, 4 20 Z" fill="var(--white)"/>
          <path d="M72 54 C 80 30, 104 18, 136 22 C 124 44, 100 56, 72 54 Z" fill="var(--white)"/>
        </svg>
        <div class="claim-text">NON-GMO</div>
      </div>
    </aside>

    <div class="divider"></div>

    <div class="brand">Nestwell</div>

    <svg class="hero-art" viewBox="0 0 320 290" role="img" aria-label="Line illustration of a mother cradling her baby inside a heart shape">
      <path d="M160 285 C 60 215, 10 160, 20 95 C 30 30, 110 10, 160 70 C 210 10, 300 30, 305 100 C 310 165, 260 215, 160 285 Z" fill="var(--figure-mid)" opacity="0.35"/>
    </svg>

    <h1 class="product-name">Nurture Plus</h1>
    <p class="tagline">Once Daly<br>Premium Multivitamin for<br>Mama &amp;Baby</p>

    <div class="count">
      <span class="count-number">90</span>
      <span class="count-unit">VAGGIE<br>CAPSULES</span>
    </div>
  </section>
</div>
</body>
</html>
```